Maplecrest Ambulatory Flyer

Need to make a flyer similar to the attached Tri Vale pdfs for Maplecrest Ambulatory. The write up is attached or can be found at https://www.medivantasc.com/bronx

Requirements
Must have
• What the existing flyer has.

```html
<!DOCTYPE html>
<html lang="en">
<head>
<meta charset="utf-8">
<title>Maplecrest Ambulatory Surgery Center Flyer</title>
<link href="https://fonts.googleapis.com/css2?family=Montserrat:wght@400;600&display=swap" rel="stylesheet">
<style>
  :root {
    --backdrop: #d6d6d6;
    --paper: #ffffff;
    --ink: #111111;
    --brand-blue: #2f5fb3;
    --photo-light: #eceef3;
    --photo-mid: #d9dde8;
    --photo-accent: #b8c8e6;
    --map-light: #e9e9e9;
    --map-dark: #8a8a8a;
  }
  * { margin: 0; padding: 0; box-sizing: border-box; }
  html, body { width: 1200px; height: 1200px; overflow: hidden; }
  body {
    background: var(--backdrop);
    font-family: "Montserrat", Arial, sans-serif;
    color: var(--ink);
    position: relative;
  }
  .page {
    position: absolute;
    top: 229px;
    width: 526px;
    height: 744px;
    background: var(--paper);
  }
  .page--front { left: 76px; }
  .page--back { left: 634px; }
  .page > * { position: absolute; }

  .brand {
    top: 62px; left: 42px; right: 42px;
    display: flex; align-items: center; gap: 12px;
  }
  .brand-mark {
    width: 22px; height: 22px; background: var(--brand-blue); flex: none;
  }
  .brand-name {
    font-size: 25px; font-weight: 600; line-height: 1.2; color: var(--ink);
  }

  .hero-photo {
    top: 224px; left: 31px; width: 458px; height: 265px;
    border: 1px solid var(--ink); border-radius: 14px;
    background: linear-gradient(115deg, var(--photo-light) 0%, var(--photo-mid) 55%, var(--photo-accent) 100%);
  }

  .body-text {
    font-size: 11px; line-height: 13.8px; letter-spacing: 0.15px;
  }
  .section-title {
    font-size: 13.6px; font-weight: 600; letter-spacing: 0.5px; line-height: 17px;
    text-transform: uppercase;
  }

  .front-intro { top: 541px; left: 48px; width: 430px; }
  .front-location-title { top: 608px; left: 48px; width: 440px; }
  .front-location-text { top: 634px; left: 48px; width: 450px; }

  .back-col { left: 44px; width: 452px; }
  .cap-title { top: 50px; }
  .cap-text { top: 96px; }
  .ben-title { top: 259px; }
  .ben-text { top: 302px; }
  .offer-title { top: 418px; }
  .offer-list {
    top: 445px; list-style: none;
    display: grid; grid-template-columns: 165px 151px auto; row-gap: 0;
  }
  .offer-list li::before { content: "• "; }
  .closing { top: 495px; width: 456px; font-weight: 600; }

  .contact { top: 586px; left: 47px; font-size: 13px; line-height: 16.5px; letter-spacing: 0.3px; }
  .contact p + p { margin-top: 16px; }
  .contact .web { letter-spacing: 3.2px; margin-top: 14px; }

  .location-map {
    top: 566px; left: 278px; width: 218px; height: 151px;
    border-radius: 12px;
    background: linear-gradient(135deg, var(--map-light) 0%, #cfcfcf 55%, var(--map-dark) 100%);
  }
</style>
</head>
<body>
  <section class="page page--front">
    <div class="brand">
      <span class="brand-mark"></span>
      <span class="brand-name">Maplecrest Ambulatory Surgery Center</span>
    </div>

    <div class="hero-photo" role="img" aria-label="Photo of a doctor in a white coat writing notes at a desk with a blue pen"></div>

    <p class="body-text front-intro">Maplecrest Ambulatory Surgery Center, is a same day surgical center, conveniently located in &nbsp;the Bronx,licensed by the state of New York and accredited by NCAHB.</p>

    <h2 class="section-title front-location-title">Convenient location for patients and surgeons</h2>
    <p class="body-text front-location-text">Maplecrest Ambulatory Surgery Center is conveniently located on Alder Avenue in the Bronx, and is easily accessed from Manhattan, Westchester and Long Island with ample parking available on site.</p>
  </section>

  <section class="page page--back">
    <h2 class="section-title back-col cap-title">Capabilities of Maplecrest Ambulatory<br>Surgery Center</h2>
    <p class="body-text back-col cap-text">Maplecrest Ambulatory Surgery Centeris a dedicated facility for same day procedures that do not require an overnight hospital stay, without sacrificing the quality of care and safety that a hospital provides. Withover 15,000 sq ft of space and four operating rooms, the centeroffers specialties including orthopedics, pain management, podiatry, ophthalmology, ENT, pediatric ENT, and general surgery. &nbsp;These same day procedures, are performed by Maplecrest Ambulatory Surgery Center’s highly skilled medical professionals that are committed to patient safety and satisfaction, providing the highest caliber of care with warmth and compassion in a personalized environment.</p>

    <h2 class="section-title back-col ben-title">Benefits of chosing Maplecrest Ambulatory<br>Surgery Center</h2>
    <p class="body-text back-col ben-text">More surgeons are choosing same day surgery centers because of the ability to provide high quality care in a state-of-the-art facility, at a more reasonable cost to you, your insurance provider, and your employer. Perhaps most importantly, same day surgery requires less down time, which means you’ll spend less time away from your family and your job, and in most instances, you can return to your daily routine the next day.</p>

    <h2 class="section-title back-col offer-title">We offer</h2>
    <ul class="body-text back-col offer-list">
      <li>Orthopedics</li>
      <li>Podiatry</li>
      <li>Adult &amp; Pediatric ENT</li>
      <li>Pain Management</li>
      <li>Ophthalmology</li>
      <li>General Surgery</li>
    </ul>

    <p class="body-text back-col closing">Here at Maplecrest Ambulatory Surgery Center, the patient is our number one priority. To offer your patients the highest caliber care for same-day surgeries, contact Maplecrest Ambulatory Surgery Center today.</p>

    <div class="contact">
      <p>2480 Alder Ave,<br>Bronx, NY 10467</p>
      <p>Phone: (718) 555-0142<br>Email: info@medivantasc.com</p>
      <p class="web">www.medivantasc.com</p>
    </div>

    <div class="location-map" role="img" aria-label="Map of the Bronx and surrounding area with a pin marking the center's address"></div>
  </section>
</body>
</html>
```